Thank You For Shopping / Hair Care Tips

I need “Thank You For Shopping”
Post cards made for my hair business !
I added pictures of post cards that I really like . I also added my LuzeKora Wigs logo for you guys to use

I want the backside of the flyer to have hair care tips !
I want people to have full directions on how to care for their wigs

Target Market(s)

Im marking to young woman to older middle aged woman
Ages 23-66 . I want my flyer to look mature And classy

Industry/Entity Type

Hair And Beauty

Font styles to use
Serif
Script

Colors
e34699
e34298
e34398

Requirements
Must have
• The flyer must have the Instagram logo with my Instagram name next to it @luze.kora.wigs__
• Also it must have my “Luze Kora Wigs” logo that I’ve uploaded in the pictures section .
• Flyer had to be two sides . One side “ thank you for shopping “ side two “hair care tips”
• My website must be on the flyer - www.luzekorawigs.example
• The flyer must match the colors of my logo
• All white . With the pink and glitter sliver you see on my logo
Nice to have
• Nice to have a glitter border
Should not have
• The flyer should not have different colors that don’t match my logo
• It shouldn’t be made without having my Instagram or website on the flyer

```html
<!DOCTYPE html>
<html lang="en">
<head>
<meta charset="utf-8">
<title>LuzeKora Wigs – Thank You / Hair Care Tips</title>
<link href="https://fonts.googleapis.com/css2?family=Playfair+Display:ital,wght@0,700;0,800;0,900;1,700&family=Roboto:ital,wght@0,400;0,500;0,700;1,400;1,500&display=swap" rel="stylesheet">
<style>
  :root {
    --pink: #d3318f;
    --charcoal: #4a4a4d;
    --paper: #efeff1;
    --ink: #333336;
    --stage: #f6f6f7;
  }
  * { box-sizing: border-box; margin: 0; padding: 0; }
  html, body { width: 1180px; height: 1200px; overflow: hidden; background: var(--stage); }
  .canvas { position: relative; width: 1180px; height: 1200px; }

  .card { position: absolute; left: 230px; width: 720px; height: 560px; overflow: hidden; }
  .card--front { top: 25px; background: var(--paper); }
  .card--back { top: 615px; background: var(--pink); }

  .front-bands { position: absolute; inset: 0; }

  .front-content { position: absolute; left: 0; width: 720px; top: 0; text-align: center; }
  .brand-name {
    position: absolute; left: 0; width: 720px; top: 95px;
    font: 700 40px "Playfair Display", serif; color: var(--pink);
  }
  .thanks {
    position: absolute; left: 0; width: 720px; top: 178px;
    font: 900 84px/80px "Playfair Display", serif; color: var(--pink);
  }
  .shopping-bar {
    position: absolute; left: 234px; top: 345px; width: 254px; height: 34px;
    background: var(--charcoal); color: #fff;
    font: 500 25px/34px "Roboto", sans-serif; letter-spacing: 2px; text-align: center;
  }
  .contact-icons { position: absolute; left: 321px; top: 397px; display: flex; gap: 8px; }
  .contact-icons svg { width: 35px; height: 35px; display: block; }
  .contact-line {
    position: absolute; left: 0; width: 720px;
    font: 700 21px "Playfair Display", serif; color: var(--ink);
  }
  .contact-line--web { top: 437px; }
  .contact-line--social { top: 466px; }

  .tips-title {
    position: absolute; left: 44px; top: 32px;
    font: 800 62px "Playfair Display", serif; color: #fff;
  }
  .tips-badge {
    position: absolute; left: 573px; top: 26px; width: 94px; height: 94px;
    border-radius: 50%; background: var(--paper);
    display: flex; align-items: center; justify-content: center; text-align: center;
    font: 700 15px/17px "Playfair Display", serif; color: var(--pink);
  }
  .tips-panel { position: absolute; left: 19px; top: 149px; width: 681px; height: 394px; background: var(--paper); }

  .tip { position: absolute; display: flex; gap: 10px; color: var(--ink); font-family: "Roboto", sans-serif; }
  .tip-num { font: 900 52px/48px "Playfair Display", serif; color: var(--pink); flex: none; }
  .tip-text { padding-top: 2px; }
  .t-xs { font-size: 10.5px; line-height: 12.5px; }
  .t-sm-b { font-size: 13px; line-height: 16px; font-weight: 700; }
  .t-md-b { font-size: 15.5px; line-height: 17.5px; font-weight: 700; }
  .t-md { font-size: 17.5px; line-height: 19px; }
  .t-it { font-size: 14px; line-height: 18px; font-style: italic; }
  .t-it-b { font-size: 13.5px; line-height: 19.5px; font-style: italic; font-weight: 500; }
  .t-lg-b { font-size: 24px; line-height: 23px; font-weight: 700; }

  .bedtime-title {
    position: absolute; left: 213px; top: 372px;
    font: 700 46px/47px "Playfair Display", serif; color: var(--ink);
  }
</style>
</head>
<body>
<div class="canvas">

  <section class="card card--front">
    <svg class="front-bands" viewBox="0 0 720 560" width="720" height="560" aria-hidden="true">
      <polygon points="0,0 221,0 85,560 0,560" fill="var(--charcoal)"/>
      <polygon points="639,0 720,0 720,560 503,560" fill="var(--pink)"/>
    </svg>
    <div class="front-content">
      <div class="brand-name">LuzeKora Wigs</div>
      <div class="thanks">Thank<br>You</div>
      <div class="shopping-bar">FOR SHOPPING</div>
      <div class="contact-icons">
        <svg viewBox="0 0 36 36" aria-label="Website">
          <circle cx="18" cy="18" r="18" fill="var(--pink)"/>
          <g fill="none" stroke="#fff" stroke-width="1.6">
            <circle cx="18" cy="18" r="10"/>
            <ellipse cx="18" cy="18" rx="4.5" ry="10"/>
            <line x1="8" y1="18" x2="28" y2="18"/>
            <line x1="10" y1="13" x2="26" y2="13"/>
            <line x1="10" y1="23" x2="26" y2="23"/>
          </g>
        </svg>
        <svg viewBox="0 0 36 36" aria-label="Social">
          <circle cx="18" cy="18" r="18" fill="var(--pink)"/>
        </svg>
      </div>
      <div class="contact-line contact-line--web">www.luzekorawigs.example</div>
      <div class="contact-line contact-line--social">@luze.kora.wigs__</div>
    </div>
  </section>

  <section class="card card--back">
    <h1 class="tips-title">Hair Care Tips</h1>
    <div class="tips-badge">LuzeKora<br>Wigs</div>
    <div class="tips-panel"></div>

    <div class="tip" style="left:44px;top:188px;width:180px">
      <span class="tip-num">1</span>
      <p class="tip-text t-xs" style="margin-left:12px">Apply a moisture rich conditioner and comb hair, starting with the ends working your way up to your scalp</p>
    </div>
    <div class="tip" style="left:230px;top:188px;width:170px">
      <span class="tip-num">2</span>
      <p class="tip-text t-md-b">Leave conditioner in for atleast 15 minutes or more.</p>
    </div>
    <div class="tip" style="left:401px;top:188px;width:125px">
      <span class="tip-num">3</span>
      <p class="tip-text t-it">Do not massage the hair</p>
    </div>
    <div class="tip" style="left:527px;top:188px;width:170px">
      <span class="tip-num">4</span>
      <p class="tip-text t-md">Rinse thoroughly</p>
    </div>

    <div class="tip" style="left:44px;top:292px;width:185px">
      <span class="tip-num">5</span>
      <p class="tip-text t-sm-b" style="margin-left:6px">Scrunch hair gently to enhance the curls(For wavy/curly patterns)</p>
    </div>
    <div class="tip" style="left:230px;top:292px;width:165px">
      <span class="tip-num">6</span>
      <p class="tip-text t-xs">When damp, apply a dime size of an anti-frizz alcohol free hair serum.</p>
    </div>
    <div class="tip" style="left:401px;top:292px;width:125px">
      <span class="tip-num">7</span>
      <p class="tip-text t-md-b" style="font-size:18px;line-height:20px">Let air dry</p>
    </div>
    <div class="tip" style="left:527px;top:292px;width:175px">
      <span class="tip-num">8</span>
      <p class="tip-text t-xs">Do not use oil product or excessive product on curly hair, it will cause matting.</p>
    </div>

    <div class="tip" style="left:40px;top:380px;width:170px">
      <span class="tip-num">9</span>
      <p class="tip-text t-it-b" style="margin-left:8px">Do not brush or comb hair when dry, it will cause hair to frizz and may cause hair to tangle.</p>
    </div>

    <div class="bedtime-title">Bed<br>Time<br>Care</div>

    <div class="tip" style="left:349px;top:380px;width:155px">
      <span class="tip-num">1</span>
      <p class="tip-text t-xs" style="margin-left:6px">Before going to bed, braid your hair into one loose large braid and wear a satin scarf or bonnet.</p>
    </div>
    <div class="tip" style="left:505px;top:380px;width:190px">
      <span class="tip-num">2</span>
      <p class="tip-text t-it-b" style="margin-left:4px">After waking up, unto braid and comb using a wide tooth comb for brush through beginning at the ends and working your way up to roots.</p>
    </div>
    <div class="tip" style="left:349px;top:460px;width:155px">
      <span class="tip-num">3</span>
      <p class="tip-text t-lg-b" style="margin-left:2px">Style as needed.</p>
    </div>
  </section>

</div>
</body>
</html>
```